Harborline Stay Collective Business Card Design

Design a business card for Harborline Stay Collective. Look at the website for colors and reference. Card should have logo, name, title, office number, mobile number, email, URL and a tagline like, "Luxury Hotel & Resort Email Marketing" (This might change).

https://www.harborlinestaycollective.net

The rest I will leave up to your imagination.

Contact Information for Business Card

Logo, name, title, office number, mobile number, email, URL and a tagline like, "Luxury Hotel & Resort Email Marketing" (This might change).

```html
<!DOCTYPE html>
<html lang="en">
<head>
<meta charset="utf-8">
<title>Harborline Stay Collective — Business Card</title>
<link href="https://fonts.googleapis.com/css2?family=Jost:wght@400;500;700&family=Cormorant+Garamond:wght@500&display=swap" rel="stylesheet">
<style>
  :root {
    --backdrop: #c8c8c8;
    --card-black: #000000;
    --ink-white: #ffffff;
    --accent-orange: #e8561a;
    --sea-teal: #2f8f98;
    --forest-green: #3f5a2c;
    --sky-slate: #5c7382;
  }
  * { margin: 0; padding: 0; box-sizing: border-box; }
  html, body { width: 1200px; height: 1000px; overflow: hidden; }
  body {
    background: var(--backdrop);
    font-family: "Jost", sans-serif;
    position: relative;
  }
  .card {
    position: absolute;
    left: 337px;
    width: 526px;
    height: 300px;
    overflow: hidden;
  }
  .card--front { top: 170px; }
  .card--back { top: 520px; background: var(--card-black); }

  .card__scenery {
    position: absolute; inset: 0;
    background:
      linear-gradient(180deg, var(--sky-slate) 0%, var(--sky-slate) 22%, transparent 40%),
      linear-gradient(100deg, var(--forest-green) 0%, #4a6a36 40%, var(--sea-teal) 62%, #3b9aa0 80%, var(--forest-green) 100%);
  }
  .card__scenery::after {
    content: ""; position: absolute; inset: 0;
    background: rgba(0, 0, 0, 0.28);
  }
  .brand {
    position: absolute;
    left: 0; right: 0; top: 118px;
    text-align: center;
    color: var(--ink-white);
  }
  .brand__name {
    font-weight: 700;
    font-size: 34px;
    letter-spacing: 1px;
    text-transform: uppercase;
  }
  .brand__tagline {
    margin-top: 8px;
    font-weight: 400;
    font-size: 13px;
    letter-spacing: 0.5px;
  }

  .person {
    position: absolute;
    left: 46px; top: 86px;
    color: var(--ink-white);
  }
  .person__name {
    font-weight: 700;
    font-size: 26px;
    letter-spacing: 0.5px;
    text-transform: uppercase;
    line-height: 1;
  }
  .person__title {
    font-family: "Cormorant Garamond", serif;
    font-weight: 500;
    font-size: 17px;
    margin-top: 3px;
  }
  .contacts {
    position: absolute;
    left: 52px; top: 172px;
    list-style: none;
    color: var(--ink-white);
    font-size: 16px;
  }
  .contacts__item {
    display: flex; align-items: center;
    height: 25px;
  }
  .contacts__icon {
    width: 14px; height: 14px;
    margin-right: 12px;
    flex: none;
  }
</style>
</head>
<body>

<section class="card card--front" aria-label="Business card front">
  <div class="card__scenery" role="img" aria-label="Coastal landscape photo with forested headland and turquoise sea"></div>
  <div class="brand">
    <div class="brand__name">Harborline Stay Collective</div>
    <div class="brand__tagline">Luxury Hotel &amp; Resort Email Marketing</div>
  </div>
</section>

<section class="card card--back" aria-label="Business card back">
  <div class="person">
    <div class="person__name">Dana Whitcombe</div>
    <div class="person__title">Chief Executive Officer</div>
  </div>
  <ul class="contacts">
    <li class="contacts__item">
      <svg class="contacts__icon" viewBox="0 0 24 24" aria-hidden="true"><path fill="var(--accent-orange)" d="M6.6 10.8a15.1 15.1 0 0 0 6.6 6.6l2.2-2.2c.3-.3.7-.4 1-.2 1.1.4 2.3.6 3.6.6.6 0 1 .4 1 1V20c0 .6-.4 1-1 1A17 17 0 0 1 3 4c0-.6.4-1 1-1h3.5c.6 0 1 .4 1 1 0 1.3.2 2.5.6 3.6.1.3 0 .7-.2 1z"/></svg>
      555.014.2387
    </li>
    <li class="contacts__item">
      <svg class="contacts__icon" viewBox="0 0 24 24" aria-hidden="true"><rect x="6" y="2" width="12" height="20" rx="2" fill="none" stroke="var(--accent-orange)" stroke-width="2.4"/><circle cx="12" cy="18" r="1.2" fill="var(--accent-orange)"/></svg>
      555.014.2387
    </li>
    <li class="contacts__item">
      <svg class="contacts__icon" viewBox="0 0 24 24" aria-hidden="true"><rect x="2" y="5" width="20" height="14" rx="1" fill="none" stroke="var(--accent-orange)" stroke-width="2.2"/><path d="M2.5 6l9.5 7 9.5-7" fill="none" stroke="var(--accent-orange)" stroke-width="2.2"/></svg>
      info@harborlinestaycollective.net
    </li>
    <li class="contacts__item">
      <svg class="contacts__icon" viewBox="0 0 24 24" aria-hidden="true"><circle cx="12" cy="12" r="10" fill="var(--accent-orange)"/><path d="M2 12h20M12 2c3 3 3 17 0 20M12 2c-3 3-3 17 0 20M4 7h16M4 17h16" fill="none" stroke="var(--card-black)" stroke-width="1.4"/></svg>
      www.harborlinestaycollective.net
    </li>
  </ul>
</section>

</body>
</html>
```